81M business card

I need a business card for a life sciences consulting firm I started. The company name is 81M and the logo is attached. I am looking for something edgey and current but different from the blah standard business card.

Industry/Entity Type

Business

Requirements
Nice to have
• Both sides

```html
<!DOCTYPE html>
<html lang="en">
<head>
<meta charset="utf-8">
<title>81M Business Card</title>
<link href="https://fonts.googleapis.com/css2?family=Open+Sans:wght@400;600;700&display=swap" rel="stylesheet">
<style>
  :root {
    --bg-light: #2b2b2b;
    --bg-dark: #040404;
    --orange: #e2590f;
    --orange-bright: #f06a14;
    --blue: #1d4f9e;
    --white: #f4f4f4;
  }
  * { margin: 0; padding: 0; box-sizing: border-box; }
  html, body {
    width: 1200px;
    height: 800px;
    overflow: hidden;
    background: var(--bg-dark);
  }
  .card {
    position: relative;
    width: 1200px;
    height: 800px;
    overflow: hidden;
    background: linear-gradient(135deg, var(--bg-light) 0%, #1c1c1c 45%, var(--bg-dark) 100%);
    font-family: "Open Sans", Arial, sans-serif;
  }
  .brand {
    position: absolute;
    left: 0;
    top: 40px;
    display: flex;
    align-items: center;
  }
  .brand-mark {
    width: 200px;
    height: 200px;
    margin-left: -2px;
    border-radius: 50%;
    background: var(--blue);
  }
  .brand-name {
    margin-left: 50px;
    font-size: 118px;
    font-weight: 700;
    line-height: 1;
    color: var(--orange);
    letter-spacing: 4px;
  }
  .brand-rule {
    position: absolute;
    left: 160px;
    top: 204px;
    width: 1040px;
    height: 8px;
    background: linear-gradient(90deg, var(--orange) 0%, var(--orange-bright) 45%, #000 70%, #000 100%);
    box-shadow: 0 2px 4px rgba(0,0,0,0.6);
  }
  .person {
    position: absolute;
    left: 100px;
    top: 352px;
    width: 500px;
    text-align: center;
  }
  .person-name {
    font-size: 29px;
    font-weight: 700;
    letter-spacing: 4px;
    color: var(--white);
    text-transform: uppercase;
  }
  .person-title {
    margin-top: 6px;
    font-size: 26px;
    font-weight: 400;
    letter-spacing: 5px;
    color: var(--orange);
  }
  .contact {
    position: absolute;
    left: 728px;
    top: 392px;
    list-style: none;
  }
  .contact-row {
    display: flex;
    align-items: baseline;
    height: 51px;
  }
  .contact-label {
    width: 104px;
    font-size: 27px;
    letter-spacing: 4px;
    color: var(--orange);
  }
  .contact-value {
    font-size: 28px;
    font-weight: 600;
    letter-spacing: 4px;
    color: var(--white);
  }
  .contact-value.small {
    font-size: 22px;
    letter-spacing: 2.5px;
    padding-left: 6px;
  }
  .footer-band {
    position: absolute;
    left: 0;
    bottom: 0;
    width: 1200px;
    height: 22px;
    background: var(--orange);
  }
</style>
</head>
<body>
<main class="card">
  <header class="brand">
    <div class="brand-mark"></div>
    <div class="brand-name">81M</div>
  </header>
  <div class="brand-rule"></div>

  <section class="person">
    <h1 class="person-name">Marina Feld</h1>
    <p class="person-title">Life Science Consultant</p>
  </section>

  <ul class="contact">
    <li class="contact-row"><span class="contact-label">Tel</span><span class="contact-value">0800 5162047</span></li>
    <li class="contact-row"><span class="contact-label">Fax</span><span class="contact-value">0800 6294815</span></li>
    <li class="contact-row"><span class="contact-label">Email</span><span class="contact-value small">81M@samplemail.com</span></li>
    <li class="contact-row"><span class="contact-label">Web</span><span class="contact-value small">81Msamplemail.com</span></li>
  </ul>

  <div class="footer-band"></div>
</main>
</body>
</html>
```